Create a business promotion flyer to leave in customer mailboxes. We are a bulk petroleum supplier, servicing any industry that requires diesel. Base in griffith NSW, servicing griffith area and surrounds.

Business Name - Terra Petro
Fuel@terrapetro-example.com.au
Marco - 0400 000 001 mtorrisi@terrapetro-example.com.au
Liam - 0400 000 002 lharcourt@terrapetro-example.com.au
Peter - 0400 000 003 pwinslow@terrapetro-example.com.au
Office 02 5550 0100

Bulk Fuel deliveries.
Oils & lubricants
Local Family owned business

```html
<!DOCTYPE html>
<html lang="en">
<head>
<meta charset="utf-8">
<title>Terra Petro – Bulk Fuel Deliveries Flyer</title>
<link rel="stylesheet" href="https://fonts.googleapis.com/css2?family=Bebas+Neue&family=Jost:wght@400;500;600&family=Montserrat:wght@500;600&display=swap">
<style>
  :root {
    --red: #ec1c24;
    --red-dark: #a3151b;
    --ink: #0d0d0d;
    --grey: #6d6e71;
    --white: #ffffff;
    --brand-grey: #58595b;
  }
  * { margin: 0; padding: 0; box-sizing: border-box; }
  html, body { width: 945px; height: 1200px; overflow: hidden; background: var(--white); }
  .flyer {
    position: relative;
    width: 945px;
    height: 1200px;
    overflow: hidden;
    background: var(--white);
    font-family: "Jost", sans-serif;
  }
  .backdrop { position: absolute; left: 0; top: 0; }
  .photo-cab {
    position: absolute;
    left: 530px; top: 66px;
    width: 415px; height: 510px;
    background: linear-gradient(180deg, #f6f6f6 0%, #e2e3e4 40%, #bfc1c4 72%, #d8d9db 100%);
    border-radius: 36px 0 0 14px;
  }
  .photo-tanker {
    position: absolute;
    left: 12px; top: 758px;
    width: 912px; height: 232px;
    background: linear-gradient(180deg, #ffffff 0%, #f1f1f2 55%, #c3c4c7 88%, #9fa0a3 100%);
    border-radius: 60px 70px 30px 30px;
    box-shadow: 0 14px 18px -10px rgba(0,0,0,0.35);
  }
  .brand {
    position: absolute;
    left: 30px; top: 96px;
  }
  .brand-name {
    display: flex; align-items: center; gap: 12px;
    font-family: "Montserrat", sans-serif;
    font-weight: 500;
    font-size: 46px;
    line-height: 1;
    color: var(--red);
    letter-spacing: -0.5px;
  }
  .brand-square { width: 22px; height: 22px; background: var(--brand-grey); }
  .brand-tagline {
    margin-top: 8px;
    margin-left: 34px;
    font-family: "Jost", sans-serif;
    font-weight: 500;
    font-size: 13px;
    letter-spacing: 2.6px;
    text-transform: uppercase;
    color: var(--brand-grey);
  }
  .headline {
    position: absolute;
    left: 28px; top: 232px;
    font-family: "Bebas Neue", sans-serif;
    font-weight: 400;
    color: var(--ink);
    font-size: 118px;
    line-height: 0.84;
    letter-spacing: 5px;
  }
  .subhead {
    position: absolute;
    left: 28px; top: 450px;
    font-family: "Bebas Neue", sans-serif;
    font-weight: 400;
    color: var(--red);
    font-size: 74px;
    letter-spacing: 3px;
    line-height: 1;
  }
  .intro {
    position: absolute;
    left: 30px; top: 538px;
    width: 466px;
    font-size: 16.5px;
    line-height: 23.5px;
    letter-spacing: 2.6px;
    color: var(--ink);
    text-align: justify;
  }
  .contacts {
    position: absolute;
    left: 30px; right: 30px; top: 1030px;
    display: grid;
    grid-template-columns: 1fr 2px 1fr 2px 1fr;
    column-gap: 8px;
    color: var(--white);
  }
  .contact { font-size: 13.5px; line-height: 22px; letter-spacing: 0.4px; white-space: nowrap; }
  .contact-name { font-weight: 600; font-size: 20px; letter-spacing: 1.5px; line-height: 24px; }
  .contact-phone { font-size: 17px; letter-spacing: 2px; }
  .contact--left { text-align: left; }
  .contact--centre { text-align: center; }
  .contact--right { text-align: right; }
  .divider { background: var(--red); width: 2px; height: 44px; margin-top: 20px; }
  .info-bar {
    position: absolute;
    left: 34px; right: 30px; top: 1134px;
    display: flex; align-items: center; gap: 12px;
    color: var(--white);
  }
  .info-label {
    font-family: "Bebas Neue", sans-serif;
    font-size: 32px; letter-spacing: 1px;
    margin-right: 4px;
  }
  .info-item { display: flex; align-items: center; gap: 9px; font-size: 21px; letter-spacing: 1px; }
  .info-item svg { flex: none; }
  .info-item--phone { font-size: 23px; letter-spacing: 2px; margin-left: 8px; }
</style>
</head>
<body>
<main class="flyer">
  <svg class="backdrop" width="945" height="1200" viewBox="0 0 945 1200" aria-hidden="true">
    <defs>
      <linearGradient id="greyField" x1="0" y1="0" x2="0" y2="1">
        <stop offset="0" stop-color="#6a6b6e"/>
        <stop offset="1" stop-color="#8c8d90"/>
      </linearGradient>
      <linearGradient id="redSweep" x1="0" y1="0" x2="1" y2="0">
        <stop offset="0" stop-color="#ec1c24"/>
        <stop offset="0.55" stop-color="#a3151b"/>
        <stop offset="1" stop-color="#ec1c24"/>
      </linearGradient>
      <linearGradient id="whiteArc" x1="0" y1="0" x2="0" y2="1">
        <stop offset="0" stop-color="#ffffff"/>
        <stop offset="0.7" stop-color="#f2f2f2"/>
        <stop offset="1" stop-color="#858689" stop-opacity="0"/>
      </linearGradient>
    </defs>
    <path d="M0,700 C250,760 600,640 945,650 L945,1200 L0,1200 Z" fill="url(#greyField)"/>
    <path d="M0,216 C180,244 330,214 470,154 C640,79 780,-6 945,-40 L945,-46 L880,-46 C740,-16 620,49 470,114 C330,179 170,212 0,194 Z" fill="#ec1c24"/>
    <path d="M0,638 C200,700 420,690 620,640 C760,605 860,585 945,588 L945,660 C840,640 720,650 600,690 C420,745 200,760 0,735 Z" fill="url(#redSweep)"/>
    <path d="M0,930 C160,800 360,724 560,722 C730,720 860,752 945,790 L945,1030 L0,1030 Z" fill="url(#whiteArc)"/>
  </svg>

  <div class="photo-cab" role="img" aria-label="Front view of a white prime mover truck with chrome grille and hazard placard"></div>
  <div class="photo-tanker" role="img" aria-label="Side view of a white fuel tanker road train with two tank trailers"></div>

  <div class="brand">
    <div class="brand-name"><span class="brand-square"></span>Terra Petro</div>
    <div class="brand-tagline">Local family owned business</div>
  </div>

  <h1 class="headline">Bulk Fuel<br>Deliveries</h1>
  <h2 class="subhead">Oils &amp; Lubricants</h2>
  <p class="intro">We are a bulk petroleum supplier, servicing any industry that requires diesel. Base in griffith NSW, servicing griffith area and surrounds.</p>

  <section class="contacts">
    <div class="contact contact--left">
      <div class="contact-name">Marco :</div>
      <div class="contact-phone">0400 000 001</div>
      <div>mtorrisi@terrapetro-example.com.au</div>
    </div>
    <span class="divider"></span>
    <div class="contact contact--centre">
      <div class="contact-name">Liam :</div>
      <div class="contact-phone">0400 000 002</div>
      <div>lharcourt@terrapetro-example.com.au</div>
    </div>
    <span class="divider"></span>
    <div class="contact contact--right">
      <div class="contact-name">Peter :</div>
      <div class="contact-phone">0400 000 003</div>
      <div>pwinslow@terrapetro-example.com.au</div>
    </div>
  </section>

  <footer class="info-bar">
    <span class="info-label">For More Info :</span>
    <span class="info-item">
      <svg width="26" height="20" viewBox="0 0 26 20" aria-hidden="true"><rect x="1.5" y="1.5" width="23" height="17" rx="3" fill="none" stroke="#fff" stroke-width="2.4"/><path d="M2.5,3 L13,11 L23.5,3" fill="none" stroke="#fff" stroke-width="2.4"/></svg>
      Fuel@terrapetro-example.com.au
    </span>
    <span class="info-item info-item--phone">
      <svg width="20" height="26" viewBox="0 0 20 26" aria-hidden="true"><path d="M10,24 C4,16 2,12 2,9 A8,8 0 0 1 18,9 C18,12 16,16 10,24 Z" fill="none" stroke="#fff" stroke-width="2.2"/><circle cx="10" cy="9" r="3" fill="none" stroke="#fff" stroke-width="2"/></svg>
      02 5550 0100
    </span>
  </footer>
</main>
</body>
</html>
```